PSD Website Design

I am looking to have a custom website designed. I would like a PSD made of the design I came up with. Once I get the design I will slice the PSD and create a wordpress template from it.

See attachment for basic layout of the graphic. The image labeled Player page is the basic page I will need for the website. I also need a home page with an image slider on it and thumbnails of recent, state video uploads.

A textured background is ok.

Looking for a quick turnaround.

Text at top of page is a menu that is needed. Open to seeing the menu as a navigational bar or/and with different font types.

No preference on page background color or font colors. I welcome creativity.

```html
<!DOCTYPE html>
<html lang="en">
<head>
<meta charset="utf-8">
<title>Summit Scouting – Player Profile</title>
<link rel="stylesheet" href="https://fonts.googleapis.com/css2?family=Open+Sans:wght@400;600;700&family=Arimo:wght@400;700&display=swap">
<style>
:root{
  --orange:#f47a20;
  --ink:#222;
  --grey:#666;
  --muted:#999;
  --link:#1a73d9;
  --green:#1a9a1a;
  --hero-bg:#ebebeb;
  --card-bg:#efefef;
  --panel:#27282c;
  --footer:#111;
  --footer-bottom:#000;
  --teal:#2f9696;
}
*{box-sizing:border-box;margin:0;padding:0}
html,body{width:1200px;height:1000px;overflow:hidden;background:#fff}
body{position:relative;font-family:Arimo,Arial,sans-serif;color:var(--ink)}
.abs{position:absolute}

/* header */
.site-header{left:0;top:0;width:1200px;height:85px;background:#fff;box-shadow:0 2px 6px rgba(0,0,0,.08);z-index:2}
.brand{left:242px;top:40px;display:flex;align-items:center;gap:7px}
.brand-dot{width:12px;height:12px;border-radius:50%;background:var(--orange)}
.brand-name{font-family:"Open Sans",sans-serif;font-weight:700;font-size:18px;line-height:22px;color:#111;letter-spacing:.3px}
.nav-item{top:56px;font-size:11px;line-height:13px;color:#555;white-space:nowrap}
.nav-sep{top:55px;width:1px;height:14px;background:#ddd}
.search{left:888px;top:45px;width:117px;height:29px;display:flex;border:1px solid #ddd;background:#fff}
.search-field{flex:1;font-size:8px;color:#888;padding:10px 9px}
.search-btn{width:32px;background:var(--orange);display:flex;align-items:center;justify-content:center}

/* hero */
.hero{left:0;top:85px;width:1200px;height:250px;background:var(--hero-bg)}
.player-photo{left:241px;top:114px;width:177px;height:185px;background:linear-gradient(180deg,#d9e8b8,#cfe0a6)}
.player-name{left:442px;top:111px;font-size:16px;font-weight:400;color:#555}
.player-pos{left:443px;top:141px;font-size:9px;font-weight:700;color:var(--link)}
.player-stats{left:443px;top:164px;font-size:8.5px;color:#777;line-height:18px}
.player-class{left:443px;top:291px;font-size:8.5px;font-weight:700;color:var(--green)}
.video{left:677px;top:114px;width:327px;height:185px;background:#0c0c0c}
.video-frame{left:10px;top:8px;width:308px;height:146px;background:linear-gradient(180deg,#d9d6d2 0%,#8e5650 55%,#3a2a2c 100%)}
.video-bar{left:6px;top:155px;width:315px;height:24px;display:flex;align-items:center;gap:6px}
.play{width:38px;height:24px;background:#2a2a2a;display:flex;align-items:center;justify-content:center}
.track{flex:1;height:18px;background:#1d1d1d;display:flex;align-items:center;padding:0 6px;gap:6px}
.track-line{flex:1;height:6px;border:1px solid #555}
.hd{font-size:9px;font-weight:700;color:#2aa6e0}

/* section headings */
.sec-title{display:flex;align-items:center;font-family:"Open Sans",sans-serif;font-size:15px;font-weight:400;color:#444}
.sec-title::before,.sec-title::after{content:"";height:2px;background:var(--orange)}
.game-title{left:241px;top:358px;width:522px}
.game-title::before{width:34px;margin-right:6px}
.game-title::after{flex:1;margin-left:6px}
.viral-title{left:776px;top:358px;width:229px}
.viral-title::before{width:20px;margin-right:8px}
.viral-title::after{flex:1;margin-left:8px}

/* video cards */
.card{width:123px;height:151px;background:var(--card-bg)}
.thumb{height:78px;position:relative;background:linear-gradient(180deg,#7aa04a,#4f7d2e)}
.thumb.alt{background:linear-gradient(135deg,#3b8fd6,#c8352b)}
.duration{position:absolute;right:8px;bottom:8px;background:#333;color:#fff;font-size:7.5px;font-weight:700;padding:3px 5px}
.card-title{font-size:9px;color:var(--link);line-height:12px;padding:8px 6px 0}
.card-meta{font-size:6.5px;color:#888;padding:7px 7px 0;display:flex;gap:9px}
.card-age{font-size:6.5px;color:#999;padding:7px 7px 0}
.divider{left:241px;top:561px;width:522px;height:1px;background:#ddd}
.channel{left:241px;top:576px;display:flex;align-items:center;gap:10px}
.channel-dot{width:14px;height:14px;border-radius:50%;background:#222}
.channel-name{font-size:11px;color:#333}
.channel-note{font-size:7px;color:#999}

/* sidebar */
.events{left:776px;top:391px;width:229px;height:288px;background:var(--panel);border-radius:2px}
.events-title{left:19px;top:22px;font-family:"Open Sans",sans-serif;font-size:16px;font-weight:600;color:#fff}
.event{left:21px;width:183px;border-bottom:1px solid #4a4b50;padding-bottom:12px}
.event-date{font-family:"Open Sans",sans-serif;font-size:13px;color:var(--orange)}
.event-text{font-size:8px;color:#ddd;line-height:13px;margin-top:5px}
.connect{left:33px;top:199px;width:151px;height:22px;background:var(--teal);color:#fff;font-size:11px;text-align:center;line-height:22px}
.socials{left:32px;top:235px;display:flex;gap:11px}
.socials span{width:30px;height:30px;border-radius:50%}

/* footer */
.footer{left:0;top:772px;width:1200px;height:186px;background:var(--footer)}
.footer-brand{left:242px;top:48px;font-family:"Open Sans",sans-serif;font-weight:700;font-size:14px;line-height:18px;color:#888;white-space:nowrap}
.footer-col{top:49px}
.footer-col h4{font-size:10px;font-weight:700;color:#ccc;margin-bottom:12px}
.footer-col li{list-style:none;font-size:8px;color:#999;line-height:15px;padding-left:2px}
.address p{font-size:8px;color:#888;line-height:10px}
.address strong{color:#888}
.address .about{margin-top:10px}
.bottom-bar{left:0;top:958px;width:1200px;height:42px;background:var(--footer-bottom)}
.bottom-nav{left:242px;top:18px;font-size:7.5px;color:#fff}
.copyright{right:190px;top:18px;font-size:7.5px;color:#888}
</style>
</head>
<body>

<header class="site-header abs">
  <div class="brand abs"><span class="brand-dot"></span><span class="brand-name">SUMMIT SCOUTING</span></div>
  <nav>
    <span class="nav-item abs" style="left:567px">Home</span>
    <span class="nav-sep abs" style="left:612px"></span>
    <span class="nav-item abs" style="left:633px">About Us</span>
    <span class="nav-sep abs" style="left:687px"></span>
    <span class="nav-item abs" style="left:710px">State</span>
    <span class="nav-sep abs" style="left:753px"></span>
    <span class="nav-item abs" style="left:773px">Position</span>
    <span class="nav-sep abs" style="left:824px"></span>
    <span class="nav-item abs" style="left:842px">Join</span>
  </nav>
  <div class="search abs">
    <div class="search-field">Search</div>
    <div class="search-btn"><svg width="10" height="10" viewBox="0 0 10 10"><circle cx="4" cy="4" r="3" fill="none" stroke="#fff" stroke-width="1.4"/><line x1="6.2" y1="6.2" x2="9" y2="9" stroke="#fff" stroke-width="1.4"/></svg></div>
  </div>
</header>

<section class="hero abs"></section>
<div class="player-photo abs" role="img" aria-label="Portrait photo of the player in a yellow sleeveless shirt"></div>
<h1 class="player-name abs">Marcus Delaney</h1>
<div class="player-pos abs">Wide Receiver</div>
<div class="player-stats abs">Harbor City, FL (Harbor Central)<br>Ht: 6-1.5 &nbsp;| &nbsp;Wt: 197<br>40 Times: 4.45<br>Vertical: 36<br>5-10-5 Shuttle: 4.42</div>
<div class="player-class abs">CLASS OF 2015</div>

<div class="video abs">
  <div class="video-frame abs" role="img" aria-label="Video still of a football team gathered at an indoor camp"></div>
  <div class="video-bar abs">
    <div class="play"><svg width="10" height="11" viewBox="0 0 10 11"><polygon points="0,0 10,5.5 0,11" fill="#fff"/></svg></div>
    <div class="track"><div class="track-line"></div><span class="hd">HD</span></div>
  </div>
</div>

<h2 class="sec-title game-title abs">GAME FILM</h2>
<h2 class="sec-title viral-title abs">TAKE IT VIRAL</h2>

<div class="card abs" style="left:242px;top:393px"><div class="thumb" role="img" aria-label="Model railway video thumbnail"><span class="duration">9.56</span></div><div class="card-title">Bergbahn Parade und weitere schöne Fahrzeuge</div><div class="card-meta"><span>by Rallmann</span><span>10,820,829 views</span></div><div class="card-age">3 years ago</div></div>
<div class="card abs" style="left:375px;top:393px"><div class="thumb" role="img" aria-label="Model railway video thumbnail"><span class="duration">9.56</span></div><div class="card-title">Bergbahn Parade und weitere schöne Fahrzeuge</div><div class="card-meta"><span>by Rallmann</span><span>10,820,829 views</span></div><div class="card-age">3 years ago</div></div>
<div class="card abs" style="left:508px;top:393px"><div class="thumb" role="img" aria-label="Model railway video thumbnail"><span class="duration">9.56</span></div><div class="card-title">Bergbahn Parade und weitere schöne Fahrzeuge</div><div class="card-meta"><span>by Rallmann</span><span>10,820,829 views</span></div><div class="card-age">3 years ago</div></div>
<div class="card abs" style="left:640px;top:393px"><div class="thumb" role="img" aria-label="Model railway video thumbnail"><span class="duration">9.56</span></div><div class="card-title">Bergbahn Parade und weitere schöne Fahrzeuge</div><div class="card-meta"><span>by Rallmann</span><span>10,820,829 views</span></div><div class="card-age">3 years ago</div></div>

<div class="divider abs"></div>
<div class="channel abs"><span class="channel-dot"></span><span class="channel-name">railtoyvideo</span><span class="channel-note">Popular channel on the web – we think you'll like it</span></div>

<div class="card abs" style="left:242px;top:605px"><div class="thumb alt" role="img" aria-label="Toy train set video thumbnail"><span class="duration">23.45</span></div><div class="card-title">Blue Engine Trackset Ultimate</div><div class="card-meta"><span>by railtoyvideo</span><span>17,498,131 views</span></div><div class="card-age">1 years ago</div></div>
<div class="card abs" style="left:375px;top:605px"><div class="thumb" role="img" aria-label="Model railway video thumbnail"><span class="duration">9.56</span></div><div class="card-title">Bergbahn Parade und weitere schöne Fahrzeuge</div><div class="card-meta"><span>by Rallmann</span><span>10,820,829 views</span></div><div class="card-age">3 years ago</div></div>
<div class="card abs" style="left:508px;top:605px"><div class="thumb" role="img" aria-label="Model railway video thumbnail"><span class="duration">9.56</span></div><div class="card-title">Bergbahn Parade und weitere schöne Fahrzeuge</div><div class="card-meta"><span>by Rallmann</span><span>10,820,829 views</span></div><div class="card-age">3 years ago</div></div>
<div class="card abs" style="left:640px;top:605px"><div class="thumb" role="img" aria-label="Model railway video thumbnail"><span class="duration">9.56</span></div><div class="card-title">Bergbahn Parade und weitere schöne Fahrzeuge</div><div class="card-meta"><span>by Rallmann</span><span>10,820,829 views</span></div><div class="card-age">3 years ago</div></div>

<aside class="events abs">
  <div class="events-title abs">NEXT EVENT</div>
  <div class="event abs" style="top:52px"><div class="event-date">17.04.2014</div><div class="event-text">Lorem Ipsum is simply dummy text of the printing and typesetting industry</div></div>
  <div class="event abs" style="top:118px"><div class="event-date">17.04.2014</div><div class="event-text">Lorem Ipsum is simply dummy text of the printing and typesetting industry</div></div>
  <div class="connect abs">CONNECT WITH STRIDE</div>
  <div class="socials abs">
    <span style="background:#3b5a9a" aria-label="Social network link"></span>
    <span style="background:#3fa7e0" aria-label="Social network link"></span>
    <span style="background:#4e6b86" aria-label="Social network link"></span>
    <span style="background:#fff" aria-label="Video channel link"></span>
  </div>
</aside>

<footer class="footer abs">
  <div class="footer-brand abs">SUMMIT SCOUTING</div>
  <div class="footer-col abs" style="left:418px"><h4>OTHER LINKS</h4><ul><li>Lorem Ipsum</li><li>Lorem Ipsum Dummy</li><li>Lorem Ipsum Text</li><li>Lorem Ipsum</li><li>Lorem Ipsum Dummy</li><li>Lorem Ipsum Text</li></ul></div>
  <div class="footer-col abs" style="left:573px"><h4>OTHER LINKS</h4><ul><li>Lorem Ipsum</li><li>Lorem Ipsum Dummy</li><li>Lorem Ipsum Text</li><li>Lorem Ipsum</li><li>Lorem Ipsum Dummy</li><li>Lorem Ipsum Text</li></ul></div>
  <div class="footer-col address abs" style="left:785px;width:190px">
    <h4>ADDRESS</h4>
    <p><strong>SUMMIT SCOUTING</strong><br>Northfield, Oak Street, 40210<br>(555) 014-2236<br>info@summitscouting.com</p>
    <p class="about">Ut eu nulla eget massa blandit eleifend vel sedis lacus. Sed at viverra nulla. Fusce vel adipisci odio. Phasellus commodo, mauris eget pharetra scelerisque, est justo lacinia tortor.</p>
  </div>
</footer>
<div class="bottom-bar abs">
  <div class="bottom-nav abs">Home &nbsp;| &nbsp;About Us &nbsp;| &nbsp;State &nbsp;| &nbsp;Position &nbsp;| &nbsp;Join</div>
  <div class="copyright abs">Privacy Policy &nbsp;| &nbsp;Copyright All Right Reserved 2014.</div>
</div>

</body>
</html>
```